Brightmoor Cleaning Services

need a brochure for my cleaning company. Contact info coming soon .

Target Market(s)

Cleaning Services

Industry/Entity Type

Cleaning Service

Requirements
Must have
• I attached logo for you to use.

Corporate address -
472 Kestrel Ridge W Ste 518
Tukwila, WA 98102

Phone number - 877-514-SHINE
Nice to have
• bifold brochure. I attached some samples
Should not have
• Pictures of people. Keep it clean and professional.

```html
<!DOCTYPE html>
<html lang="en">
<head>
<meta charset="utf-8">
<title>Brightmoor Cleaning Services – Bifold Brochure</title>
<link rel="stylesheet" href="https://fonts.googleapis.com/css2?family=Open+Sans:wght@400;700&family=Advent+Pro:wght@300&family=Playfair+Display:wght@400&display=swap">
<style>
  :root{
    --board:#6fb1e0;
    --brand-blue:#0070b9;
    --paper:#ffffff;
    --ink:#1a1a1a;
    --art-warm:#e9b45a;
    --art-cool:#e1463b;
  }
  *{margin:0;padding:0;box-sizing:border-box}
  html,body{width:1200px;height:1191px;overflow:hidden;background:var(--board)}
  .board{position:relative;width:1200px;height:1191px}
  .side-label{position:absolute;font-family:"Playfair Display",serif;font-weight:400;font-size:47px;color:var(--paper);line-height:1}
  .side-label--inside{left:35px;top:70px}
  .side-label--outside{left:607px;top:67px}

  .spread{position:absolute;background:var(--paper);overflow:hidden}
  .spread--inside{left:32px;top:116px;width:549px;height:384px}
  .spread--outside{left:606px;top:114px;width:543px;height:386px}

  .panel-blue{position:absolute;background:var(--brand-blue)}
  .spread--inside .panel-blue{left:0;top:0;width:267px;height:100%}
  .spread--outside .panel-blue{left:280px;top:0;width:263px;height:287px}

  .brand-name{position:absolute;font-family:"Open Sans",sans-serif;font-weight:700;color:var(--paper);text-align:center;line-height:1.1}
  .spread--inside .brand-name{left:0;width:267px;top:70px;font-size:26px}
  .spread--outside .brand-name{left:280px;width:263px;top:104px;font-size:26px}
  .brand-name--small{color:var(--brand-blue);font-size:9px !important}
  .spread--outside .brand-name--small{left:96px;width:100px;top:312px}

  .tagline{position:absolute;font-family:"Advent Pro",sans-serif;font-weight:300;text-align:center;font-size:16px;line-height:20px;letter-spacing:.6px}
  .tagline .small-caps{font-variant:small-caps}
  .tagline::after{content:"";position:absolute;left:50%;transform:translateX(-50%);bottom:-5px;width:78px;height:2px;background:currentColor}
  .spread--inside .tagline{left:0;width:267px;top:212px;color:var(--paper)}
  .spread--outside .tagline{left:300px;width:226px;top:307px;color:var(--brand-blue)}

  .contact-list{position:absolute;left:70px;top:272px;list-style:none;font-family:"Advent Pro",sans-serif;font-size:7.5px;color:var(--paper);letter-spacing:.5px}
  .contact-list li{display:flex;align-items:center;height:16px;margin-bottom:3px}
  .contact-list svg{width:16px;height:16px;margin-right:8px;flex:none}

  .section{position:absolute;left:289px;width:150px;font-family:"Open Sans",sans-serif;color:var(--ink)}
  .section h2{font-weight:400;font-size:10.5px;padding-left:2px;padding-bottom:4px;border-bottom:2px solid var(--brand-blue);width:81px;margin-bottom:7px}
  .section p{font-size:5.6px;line-height:7.8px}
  .section .credit{text-align:right;padding-right:6px;margin-bottom:6px}
  .section--who{top:54px}
  .section--what{top:110px}
  .section--text{top:172px}
  .section--quote{left:388px;top:245px;width:128px}

  .art-slot{position:absolute;border-radius:4px;background:linear-gradient(135deg,var(--art-warm),var(--art-cool))}
  .art-slot--inside{left:290px;top:258px;width:78px;height:73px}
  .art-slot--outside{left:82px;top:94px;width:127px;height:121px}

  .footer-line{position:absolute;font-family:"Advent Pro",sans-serif;font-size:7px;color:var(--brand-blue);letter-spacing:.5px;white-space:nowrap}
  .spread--inside .footer-line{left:273px;top:370px}
  .spread--outside .footer-line{left:23px;top:373px}
  .cover-address{position:absolute;left:290px;width:246px;top:356px;text-align:center;font-family:"Advent Pro",sans-serif;font-size:7px;line-height:10px;color:var(--brand-blue);letter-spacing:.5px}
</style>
</head>
<body>
<main class="board">
  <h1 class="side-label side-label--inside">Inside</h1>
  <section class="spread spread--inside">
    <div class="panel-blue"></div>
    <div class="brand-name">Brightmoor<br>Cleaning Services</div>
    <div class="tagline">PROFESIONAL<br><span class="small-caps">Cleaning Services</span></div>
    <ul class="contact-list">
      <li><svg viewBox="0 0 16 16"><circle cx="8" cy="8" r="7" fill="none" stroke="#fff" stroke-width="1.5"/></svg>WA 98102</li>
      <li><svg viewBox="0 0 16 16"><path d="M4 3l3 0 1 3-1.5 1.2a7 7 0 0 0 3.3 3.3L11 9l3 1v3c-6 0-10-4-10-10z" fill="#fff"/></svg>877-514-SHINE</li>
      <li><svg viewBox="0 0 16 16"><path d="M8 1a5 5 0 0 0-5 5c0 4 5 9 5 9s5-5 5-9a5 5 0 0 0-5-5z" fill="none" stroke="#fff" stroke-width="1.6"/><circle cx="8" cy="6" r="1.8" fill="#fff"/></svg>472 Kestrel Ridge W Ste 518 Tukwila</li>
    </ul>

    <div class="section section--who"><h2>Who we are</h2><p>your text your text your text your text your text<br>your text your text your text your text your text<br>your textyour textyour textyour text</p></div>
    <div class="section section--what"><h2>What we can</h2><p>your text your text your text your text your text<br>your text your text your text your text your text<br>your textyour textyour textyour text</p></div>
    <div class="section section--text"><h2>Text</h2><p>your text your text your text your text your text<br>your text your text your text your text your text<br>your textyour textyour textyour text</p></div>
    <div class="section section--quote"><h2>Text</h2>
      <p>your text your text your text your text your text<br>your text your text your text your text your text<br>your textyour textyour textyour text</p><p class="credit">- Ivo</p>
      <p>your text your text your text your text your text<br>your text your text your text your text your text<br>your textyour textyour textyour text</p><p class="credit">- Ivo</p>
    </div>
    <div class="art-slot art-slot--inside" role="img" aria-label="Illustration of cleaning supplies: mops, broom, gloves, spray bottles, bucket and caution sign"></div>
    <p class="footer-line">472 Kestrel Ridge W Ste 518 Tukwila | WA 98102| Phone number - 877-514-SHINE</p>
  </section>

  <h1 class="side-label side-label--outside">Outside</h1>
  <section class="spread spread--outside">
    <div class="art-slot art-slot--outside" role="img" aria-label="Illustration of cleaning supplies: mops, broom, gloves, spray bottles, bucket and caution sign"></div>
    <div class="brand-name brand-name--small">Brightmoor<br>Cleaning Services</div>
    <p class="footer-line">472 Kestrel Ridge W Ste 518 Tukwila | WA 98102| Phone number - 877-514-SHINE</p>
    <div class="panel-blue"></div>
    <div class="brand-name">Brightmoor<br>Cleaning Services</div>
    <div class="tagline">PROFESIONAL<br><span class="small-caps">Cleaning Services</span></div>
    <p class="cover-address">472 Kestrel Ridge W Ste 518 Tukwila<br>|WA 98102| Phone number - 877-514-SHINE</p>
  </section>
</main>
</body>
</html>
```